Global lighting company needs compelling e-tail graphic

Our company is a global lighting company that sells light bulbs, lighting fixtures and ceiling fans. For this project, we have a concept developed for a graphic that explains color temperature for LED light bulbs. We would like to develop this concept into something more exciting and polished for consumer-friendly use on our e-tail product pages.Color temperature, in simple terms, is the ambience and atmosphere created by the color of a light bulb. More detailed information about color temperature can be found here: http://www.brantmoorlamps.com/color-temperature.aspx

Target Market(s)

Online consumers, homeowners

Industry/Entity Type

Lighting Fixture

Font styles to use
Sans Serif

Colors

Designer to choose colors to be used in the design.

Requirements
Must have
• Images depicting color temperature, preferably residential room scenes

```html
<!DOCTYPE html>
<html lang="en">
<head>
<meta charset="utf-8">
<title>Color Temperature Guide</title>
<link href="https://fonts.googleapis.com/css2?family=Roboto+Condensed:wght@300;400&display=swap" rel="stylesheet">
<style>
  :root {
    --ink: #2b2b2b;
    --paper: #ffffff;
    --label: #ffffff;
    --dusk-top: #3b352d;
    --dusk-bottom: #2f2c28;
    --warm-1: #f6d59a;
    --warm-2: #c98a3c;
    --neutral-1: #f5ecd6;
    --neutral-2: #a98a55;
    --cool-1: #efece6;
    --cool-2: #8f8a75;
  }
  * { margin: 0; padding: 0; box-sizing: border-box; }
  html, body { width: 1200px; height: 1200px; overflow: hidden; background: var(--dusk-bottom); }
  .canvas {
    position: relative;
    width: 1200px;
    height: 1200px;
    overflow: hidden;
    font-family: "Roboto Condensed", "Arial Narrow", sans-serif;
  }
  .backdrop {
    position: absolute; left: 0; width: 1200px;
  }
  .backdrop--top {
    top: 0; height: 270px;
    background: radial-gradient(ellipse 140px 80px at 525px 80px, #4a4640 0%, #4a4640 95%, transparent 100%),
                linear-gradient(180deg, var(--dusk-top), #36312a);
  }
  .backdrop--bottom {
    top: 930px; height: 270px;
    background: linear-gradient(180deg, #3a362f, var(--dusk-bottom));
  }
  .sheet {
    position: absolute; left: 0; top: 270px; width: 1200px; height: 622px;
    background: var(--paper);
  }
  .headline {
    position: absolute; left: 38px; top: 302px; width: 1126px;
    font-weight: 300; font-size: 39px; line-height: 1;
    color: var(--ink); white-space: nowrap;
    text-align: justify; text-align-last: justify;
  }
  .scene {
    position: absolute; top: 364px; width: 352px; height: 528px;
    overflow: hidden;
  }
  .scene--warm { left: 38px; background: linear-gradient(180deg, var(--warm-1) 0%, #f3e0a8 45%, var(--warm-2) 100%); }
  .scene--neutral { left: 425px; background: linear-gradient(180deg, var(--neutral-1) 0%, #f7f0dc 45%, var(--neutral-2) 100%); }
  .scene--cool { left: 811px; background: linear-gradient(180deg, var(--cool-1) 0%, #f4f3ef 45%, var(--cool-2) 100%); }
  .scene__label {
    position: absolute; left: 0; right: 0; bottom: 14px;
    text-align: center; color: var(--label);
    font-weight: 300; font-size: 28px; letter-spacing: 0.2px;
    white-space: nowrap;
  }
  .spectrum {
    position: absolute; left: 0; top: 892px; width: 1200px; height: 38px;
    background: linear-gradient(90deg, #f08470 0%, #f9a96a 14%, #fbcd70 30%, #fbe37a 45%, #fdf7b0 65%, #fffbe6 78%, #ffffff 84%, #cfe9f7 92%, #8ccdf0 100%);
  }
  .spectrum__mark {
    position: absolute; top: 0; height: 38px; line-height: 38px;
    transform: translateX(-50%);
    font-size: 27px; font-weight: 300; color: #1e1e1e; white-space: nowrap;
  }
</style>
</head>
<body>
<div class="canvas">
  <div class="backdrop backdrop--top" role="img" aria-label="Dimmed photo of a tatami room ceiling with a round light fixture"></div>
  <div class="backdrop backdrop--bottom" role="img" aria-label="Dimmed photo of a tatami mat floor"></div>
  <div class="sheet"></div>

  <h1 class="headline">COLOR TEMPERATURE AFFECTS THE MOOD AND AMBIENCE OF A ROOM</h1>

  <div class="scene scene--warm" role="img" aria-label="Tatami room lit by warm amber ceiling light">
    <p class="scene__label">COZY, CALM, INVITING</p>
  </div>
  <div class="scene scene--neutral" role="img" aria-label="Tatami room lit by neutral white ceiling light">
    <p class="scene__label">BRIGHT, VIBRANT</p>
  </div>
  <div class="scene scene--cool" role="img" aria-label="Tatami room lit by cool daylight ceiling light">
    <p class="scene__label">CRISP, INVIGORATING</p>
  </div>

  <div class="spectrum">
    <span class="spectrum__mark" style="left:213px">2700K - 3000K</span>
    <span class="spectrum__mark" style="left:610px">4000K</span>
    <span class="spectrum__mark" style="left:986px">5000K</span>
  </div>
</div>
</body>
</html>
```